Baby acupressure app for parents

We need an app for parents that teaches parents how to help them relieve their baby's imbalances (stomach ache, trouble sleeping etc.)

Please see the attached document (with info) and wireframes.

This project is urgent so please only participate if you're able to finish all screens within a few days after the contest is over.

Target Market(s)

Baby moms (20-40 years of age)

Industry/Entity Type

Baby Care

Colors
886aae
b768aa
e667a6
f68d4d
faa54b
fac994
f9ba93
f59195
fee18a

Requirements
Must have
• A high quality design that is both modern and very sleek and stylish.
Nice to have
• Simple animations to make the app "feel" like it's extreme high quality and make the user want to use it again and again
Should not have
• Sandwich menus

```html
<!DOCTYPE html>
<html lang="en">
<head>
<meta charset="utf-8">
<title>Nuzzle Nook – app screens</title>
<link href="https://fonts.googleapis.com/css2?family=Montserrat:wght@400;500;600;700;800&display=swap" rel="stylesheet">
<style>
:root{
  --bg:#ece2ee;
  --purple:#8c62c6;
  --purple-soft:#b79ad9;
  --purple-deep:#7650b0;
  --ink:#3a3340;
  --muted:#8a8290;
  --line:#e6e1ea;
  --white:#ffffff;
  --green:#c9f59a;
  --periwinkle:#b6b9f6;
  --pink:#f6aee4;
  --cyan:#aeeef6;
  --yellow:#f7ee7a;
  --mint:#7eeec9;
  --rose:#f9c4e6;
  --photo-warm:#d9b9a8;
  --photo-cool:#e6d6d0;
}
*{box-sizing:border-box;margin:0;padding:0}
html,body{width:1200px;height:750px;overflow:hidden}
body{background:var(--bg);font-family:"Montserrat",sans-serif;color:var(--ink);position:relative}
.grid{position:absolute;left:40px;top:18px;display:grid;grid-template-columns:repeat(4,200px);grid-template-rows:350px 350px;gap:14px 28px}
.screen{width:200px;height:350px;background:var(--white);border-radius:10px;overflow:hidden;position:relative;display:flex;flex-direction:column;box-shadow:0 6px 18px rgba(120,80,160,.15)}
.bar{height:34px;background:var(--purple);color:var(--white);font-size:8px;font-weight:600;letter-spacing:.8px;display:flex;align-items:center;justify-content:center;position:relative;flex:none}
.bar .back{position:absolute;left:10px;top:11px}
.bar .restore{position:absolute;right:8px;top:6px;font-size:5px;font-weight:500;letter-spacing:0;display:flex;flex-direction:column;align-items:center;gap:1px}
.body{flex:1;padding:8px 10px;overflow:hidden}
.tabs{height:36px;border-top:1px solid var(--line);display:flex;justify-content:space-around;align-items:center;flex:none}
.tab{display:flex;flex-direction:column;align-items:center;gap:2px;font-size:6px;color:var(--muted)}
.tab.on{color:var(--purple)}
.tab svg{width:11px;height:11px}
/* imbalances */
.ill{border-radius:4px;padding:6px 8px;margin-bottom:5px}
.ill h3{font-size:8px;font-weight:700;letter-spacing:.3px}
.ill p{font-size:6px;color:#5b5460;margin-top:1px}
.colic{background:var(--green)}.growing{background:var(--periwinkle)}.cold{background:var(--pink)}
.ear{background:var(--cyan)}.eczema{background:var(--yellow)}.reflux{background:var(--mint)}
/* spots */
.lead{font-size:6.5px;font-weight:600;line-height:1.4;margin-bottom:6px}
.spots{display:grid;grid-template-columns:1fr 1fr;gap:6px}
.spot{border-radius:6px;background:#f6f3f8;height:74px;position:relative;display:flex;flex-direction:column;align-items:center;justify-content:flex-end;padding-bottom:5px}
.spot .art{width:32px;height:30px;border-radius:6px;background:#e3dbea;margin-bottom:5px}
.spot b{font-size:7px;color:var(--purple);font-weight:600}
.spot small{font-size:5px;color:var(--muted)}
.spot .tag{position:absolute;top:0;right:8px;font-size:5px;padding:2px 3px;border-radius:0 0 3px 3px}
.t1{background:var(--cyan)}.t2{background:var(--mint)}.t3{background:var(--yellow)}.t4{background:var(--pink)}
.expert{margin-top:7px;height:40px;border-radius:6px;background:var(--rose);display:flex;align-items:center;justify-content:space-between;padding:0 6px}
.expert p{font-size:5.5px;font-weight:600}
.expert strong{display:block;font-size:9px;color:#e0459d;font-weight:600}
.expert .avatar{width:28px;height:34px;border-radius:4px;background:linear-gradient(#f08ac6,#d9a6c8)}
/* intro */
.copy{font-size:6px;line-height:1.5;color:#5b5460;margin-bottom:6px}
.media{border-radius:6px;position:relative;display:flex;align-items:center;justify-content:center}
.media.baby{height:100px;background:linear-gradient(135deg,#c9b3a3,#a99587)}
.play{width:24px;height:24px;border-radius:50%;background:rgba(255,255,255,.75);display:flex;align-items:center;justify-content:center}
/* splash */
.splash{background:linear-gradient(160deg,#b79ad9,#9a78cc);align-items:center;justify-content:center;color:var(--white)}
.brand{font-size:11px;font-weight:700;letter-spacing:1.5px;display:flex;align-items:center;gap:6px}
.brand i{width:10px;height:10px;border-radius:50%;background:currentColor;display:inline-block}
/* detail */
.media.nap{height:70px;background:linear-gradient(135deg,var(--photo-cool),var(--photo-warm))}
.media.touch{height:58px;background:linear-gradient(135deg,#e8ddd7,#c8ada0);margin-bottom:6px}
.btn{display:block;margin:0 auto;width:fit-content;background:var(--purple);color:var(--white);font-size:7px;font-weight:600;border-radius:12px;padding:5px 14px}
/* welcome */
.welcome{background:linear-gradient(170deg,#b59bd6,#9676c8);color:var(--white);align-items:center;padding:0 16px}
.welcome .brand{margin-top:110px}
.welcome .sub{font-size:7px;opacity:.85;margin:6px 0 18px}
.welcome .btn{background:var(--purple-deep)}
.welcome .fine{position:absolute;bottom:16px;left:16px;right:16px;font-size:5px;opacity:.7;text-align:center;line-height:1.5}
/* upgrade */
.card{border-radius:8px;background:#f4f1f7;padding:8px;margin-bottom:8px;position:relative}
.badge{position:absolute;left:8px;top:10px;width:34px;height:34px;border-radius:50%;border:2px solid var(--purple);font-size:7px;font-weight:800;color:var(--purple);display:flex;align-items:center;justify-content:center;text-align:center;line-height:1}
.deal{text-align:right;color:var(--purple)}
.deal small{font-size:6px;font-weight:600}
.deal .time{font-size:11px;font-weight:700;color:var(--ink)}
.deal .price{font-size:16px;font-weight:800}
.ready{font-size:9px;font-weight:700;color:var(--purple);text-align:center;margin-top:6px}
.perks{font-size:5.5px;color:var(--muted);text-align:center;line-height:1.5;margin:3px 0 6px}
.bonus{text-align:center}
.bonus h4{font-size:10px;font-weight:700}
.bonus p{font-size:6.5px;color:var(--purple);font-weight:600;margin-top:3px}
.bonus span{font-size:6.5px;font-weight:600}
.bonus em{font-style:normal;color:var(--purple);font-weight:700;font-size:8px}
.mark{position:absolute;right:40px;top:40px;color:var(--purple);display:flex;align-items:center;gap:10px;font-size:22px;font-weight:700;letter-spacing:1px}
.mark i{width:16px;height:16px;border-radius:50%;background:var(--purple)}
</style>
</head>
<body>

<div class="mark"><i></i>NUZZLE NOOK</div>

<div class="grid">

  <!-- Imbalances -->
  <section class="screen">
    <header class="bar">IMBALANCES</header>
    <div class="body">
      <div class="ill colic"><h3>COLIC</h3><p>Long and frequent crying is hard to deal with</p></div>
      <div class="ill growing"><h3>GROWING PAINS</h3><p>Relieve pain that comes from growth spurts</p></div>
      <div class="ill cold"><h3>COLD, COUGHING ETC.</h3><p>Winter time can be hard - help out your baby</p></div>
      <div class="ill ear"><h3>EAR PAIN</h3><p>Oh, those little ears can hurt so much</p></div>
      <div class="ill eczema"><h3>ECZEMA</h3><p>Relieve pain that comes from growth spurts</p></div>
      <div class="ill reflux"><h3>REFLUX</h3><p>Relieve pain that comes from growth spurts</p></div>
    </div>
    <nav class="tabs">
      <span class="tab on"><svg viewBox="0 0 12 12"><path d="M1 6 6 1.5 11 6M2.5 5v5.5h7V5" fill="none" stroke="currentColor"/></svg>Home</span>
      <span class="tab"><svg viewBox="0 0 12 12"><circle cx="6" cy="6" r="5" fill="none" stroke="currentColor"/><path d="M3.5 7q2.5 2 5 0" fill="none" stroke="currentColor"/></svg>Imbalances</span>
      <span class="tab"><svg viewBox="0 0 12 12"><circle cx="9" cy="2.5" r="1.5" fill="currentColor"/><circle cx="3" cy="6" r="1.5" fill="currentColor"/><circle cx="9" cy="9.5" r="1.5" fill="currentColor"/><path d="M9 2.5 3 6l6 3.5" fill="none" stroke="currentColor"/></svg>Share</span>
      <span class="tab"><svg viewBox="0 0 12 12"><circle cx="6" cy="2.5" r="1" fill="currentColor"/><path d="M6 5v6" stroke="currentColor" stroke-width="1.4"/></svg>About</span>
    </nav>
  </section>

  <!-- Ear pain spots -->
  <section class="screen">
    <header class="bar"><svg class="back" width="12" height="10" viewBox="0 0 12 10"><path d="M11 5H1m4-4L1 5l4 4" fill="none" stroke="#fff" stroke-width="1.2"/></svg>EAR PAIN</header>
    <div class="body">
      <p class="lead">There are multiple ways to help relieve your child's ear pain. Select a spot to get started...</p>
      <div class="spots">
        <div class="spot"><span class="tag t1">15min</span><span class="art" role="img" aria-label="Outline drawing of a child's body"></span><b>Body</b><small>Everyday</small></div>
        <div class="spot"><span class="tag t2">10min</span><span class="art" role="img" aria-label="Outline drawing of a baby's head"></span><b>Face</b><small>Everyday</small></div>
        <div class="spot"><span class="tag t3">15min</span><span class="art" role="img" aria-label="Outline drawing of two small feet"></span><b>Feet</b><small>Everyday</small></div>
        <div class="spot"><span class="tag t4">10min</span><span class="art" role="img" aria-label="Outline drawing of a small hand"></span><b>Hand</b><small>Everyday</small></div>
      </div>
      <div class="expert">
        <p>Get some additional advice from<strong>Mira Holt</strong></p>
        <span class="avatar" role="img" aria-label="Portrait photo of the advisor"></span>
      </div>
    </div>
    <nav class="tabs">
      <span class="tab on"><svg viewBox="0 0 12 12"><path d="M1 6 6 1.5 11 6M2.5 5v5.5h7V5" fill="none" stroke="currentColor"/></svg>Home</span>
      <span class="tab"><svg viewBox="0 0 12 12"><circle cx="6" cy="6" r="5" fill="none" stroke="currentColor"/><path d="M3.5 7q2.5 2 5 0" fill="none" stroke="currentColor"/></svg>Imbalances</span>
      <span class="tab"><svg viewBox="0 0 12 12"><circle cx="9" cy="2.5" r="1.5" fill="currentColor"/><circle cx="3" cy="6" r="1.5" fill="currentColor"/><circle cx="9" cy="9.5" r="1.5" fill="currentColor"/><path d="M9 2.5 3 6l6 3.5" fill="none" stroke="currentColor"/></svg>Share</span>
      <span class="tab"><svg viewBox="0 0 12 12"><circle cx="6" cy="2.5" r="1" fill="currentColor"/><path d="M6 5v6" stroke="currentColor" stroke-width="1.4"/></svg>About</span>
    </nav>
  </section>

  <!-- Intro -->
  <section class="screen">
    <header class="bar">NUZZLE NOOK</header>
    <div class="body">
      <p class="copy">Some intro text about the app, its content and a little text about the author. Some intro text about the app and how it works for parents.</p>
      <p class="copy">How to use the app and how the spots work (preview some treatments and purchase others). Select "Imbalances" in the menu to get started!</p>
      <div class="media baby" role="img" aria-label="Photo of a baby sitting in a knitted hat">
        <span class="play"><svg width="10" height="10" viewBox="0 0 10 10"><path d="M2 1l7 4-7 4z" fill="#8c62c6"/></svg></span>
      </div>
    </div>
    <nav class="tabs">
      <span class="tab on"><svg viewBox="0 0 12 12"><path d="M1 6 6 1.5 11 6M2.5 5v5.5h7V5" fill="none" stroke="currentColor"/></svg>Home</span>
      <span class="tab"><svg viewBox="0 0 12 12"><circle cx="6" cy="6" r="5" fill="none" stroke="currentColor"/><path d="M3.5 7q2.5 2 5 0" fill="none" stroke="currentColor"/></svg>Imbalances</span>
      <span class="tab"><svg viewBox="0 0 12 12"><circle cx="9" cy="2.5" r="1.5" fill="currentColor"/><circle cx="3" cy="6" r="1.5" fill="currentColor"/><circle cx="9" cy="9.5" r="1.5" fill="currentColor"/><path d="M9 2.5 3 6l6 3.5" fill="none" stroke="currentColor"/></svg>Share</span>
      <span class="tab"><svg viewBox="0 0 12 12"><circle cx="6" cy="2.5" r="1" fill="currentColor"/><path d="M6 5v6" stroke="currentColor" stroke-width="1.4"/></svg>About</span>
    </nav>
  </section>

  <!-- Splash -->
  <section class="screen splash">
    <div class="brand"><i></i>NUZZLE NOOK</div>
  </section>

  <!-- Ear pain detail -->
  <section class="screen">
    <header class="bar"><svg class="back" width="12" height="10" viewBox="0 0 12 10"><path d="M11 5H1m4-4L1 5l4 4" fill="none" stroke="#fff" stroke-width="1.2"/></svg>EAR PAIN</header>
    <div class="body">
      <div class="media nap" role="img" aria-label="Photo of a sleeping newborn">
        <span class="play"><svg width="10" height="10" viewBox="0 0 10 10"><path d="M2 1l7 4-7 4z" fill="#8c62c6"/></svg></span>
      </div>
      <p class="copy" style="margin-top:6px">This is some text about the specific imbalance. What could be the reasons for it, is it normal, symptoms etc.</p>
      <div class="media touch" role="img" aria-label="Photo of a hand gently pressing a spot near a baby's ear"></div>
      <p class="copy">There are multiple ways to trigger some positive effects and you can try our multiple spots. Also check out the bonus video.</p>
      <span class="btn">Start now</span>
    </div>
    <nav class="tabs">
      <span class="tab on"><svg viewBox="0 0 12 12"><path d="M1 6 6 1.5 11 6M2.5 5v5.5h7V5" fill="none" stroke="currentColor"/></svg>Home</span>
      <span class="tab"><svg viewBox="0 0 12 12"><circle cx="6" cy="6" r="5" fill="none" stroke="currentColor"/><path d="M3.5 7q2.5 2 5 0" fill="none" stroke="currentColor"/></svg>Imbalances</span>
      <span class="tab"><svg viewBox="0 0 12 12"><circle cx="9" cy="2.5" r="1.5" fill="currentColor"/><circle cx="3" cy="6" r="1.5" fill="currentColor"/><circle cx="9" cy="9.5" r="1.5" fill="currentColor"/><path d="M9 2.5 3 6l6 3.5" fill="none" stroke="currentColor"/></svg>Share</span>
      <span class="tab"><svg viewBox="0 0 12 12"><circle cx="6" cy="2.5" r="1" fill="currentColor"/><path d="M6 5v6" stroke="currentColor" stroke-width="1.4"/></svg>About</span>
    </nav>
  </section>

  <!-- Welcome -->
  <section class="screen welcome">
    <div class="brand"><i></i>NUZZLE NOOK</div>
    <p class="sub">Help relieve your child's imbalances</p>
    <span class="btn">Lets get started</span>
    <p class="fine">Always consult a physician if you suspect your child is ill. Read our terms and FAQ for more info.</p>
  </section>

  <!-- Upgrade -->
  <section class="screen">
    <header class="bar"><svg class="back" width="12" height="10" viewBox="0 0 12 10"><path d="M11 5H1m4-4L1 5l4 4" fill="none" stroke="#fff" stroke-width="1.2"/></svg>UPGRADE
      <span class="restore"><svg width="9" height="9" viewBox="0 0 10 10"><path d="M2 5a3 3 0 1 0 1-2.2M1.5 1v2.5H4" fill="none" stroke="#fff"/></svg>Restore Purchases</span>
    </header>
    <div class="body">
      <div class="card">
        <span class="badge">15%<br>off</span>
        <div class="deal"><small>Deal off</small><div class="time">12:06:30</div><div class="price">99 kr.</div></div>
        <div class="ready">Ready for anything!</div>
        <p class="perks">All 12 imbalances · All bonus spots<br>All current &amp; upcoming videos</p>
        <span class="btn">Get full access!</span>
      </div>
      <div class="card bonus">
        <h4>Ear pain bonus</h4>
        <p>Unlock all spots for "Ear pain"</p>
        <span>Just only </span><em>39 kr.</em>
      </div>
    </div>
    <nav class="tabs">
      <span class="tab on"><svg viewBox="0 0 12 12"><path d="M1 6 6 1.5 11 6M2.5 5v5.5h7V5" fill="none" stroke="currentColor"/></svg>Home</span>
      <span class="tab"><svg viewBox="0 0 12 12"><circle cx="6" cy="6" r="5" fill="none" stroke="currentColor"/><path d="M3.5 7q2.5 2 5 0" fill="none" stroke="currentColor"/></svg>Imbalances</span>
      <span class="tab"><svg viewBox="0 0 12 12"><circle cx="9" cy="2.5" r="1.5" fill="currentColor"/><circle cx="3" cy="6" r="1.5" fill="currentColor"/><circle cx="9" cy="9.5" r="1.5" fill="currentColor"/><path d="M9 2.5 3 6l6 3.5" fill="none" stroke="currentColor"/></svg>Share</span>
      <span class="tab"><svg viewBox="0 0 12 12"><circle cx="6" cy="2.5" r="1" fill="currentColor"/><path d="M6 5v6" stroke="currentColor" stroke-width="1.4"/></svg>About</span>
    </nav>
  </section>

</div>
</body>
</html>
```